Modern, cutting edge crypto trading website.

I need a single-page website design, approximate 4-5 pages. I have included a screenshot of the inside of the current application for some reference for what it currently looks like. This is the public side of the application for not logged in users.

I am currently thinking about 3-5 sections of the page.
Menu at top is optional, these could be the sections of the site.
1. Above the fold cool, grabbing stuff.
2. What problem does this solve
3. Additional benefits
4. Pricing
5. Open to ideas! Well it's all open to ideas if you have ideas.

I am nervous about hiring designers, I am open to a further discussion for more work for additional money but I have to LIKE your design. So this could be considered a trial. I would like to continue to design the application itself and match everything together!

I really like the tradewisp website.

Competitor websites:
https://7ridges.example/
https://www.tradewisp.example/

Target Market(s)

Adults 25-50 mostly male,

Number of Pages Required

4 page

Colors

Designer to choose colors to be used in the design.

Requirements
Must have
• Modern design, clean lines, professional.
Nice to have
• Fun SVG stuff. Not for this price, but in the future.
Should not have
• Should not be cluttered OR too spacey. Quince's website has too much open space sometimes.

```html
<!DOCTYPE html>
<html lang="en">
<head>
<meta charset="utf-8">
<title>SignalForge – Crypto Trading</title>
<link href="https://fonts.googleapis.com/css2?family=Raleway:wght@300;400;600;700;800&family=Poppins:wght@300;400;500;600&family=Archivo+Black&display=swap" rel="stylesheet">
<style>
:root{
  --blue:#1f8ad6;
  --blue-dark:#1565b4;
  --navy:#0c1a33;
  --ink:#243447;
  --text:#5c6670;
  --sky:#e7f4fc;
  --sky-row:#c9e7f7;
  --white:#fff;
  --line:#d5e5f0;
}
*{margin:0;padding:0;box-sizing:border-box}
html,body{width:1200px;height:4068px;overflow:hidden}
body{position:relative;font-family:"Poppins",sans-serif;color:var(--text);background:var(--white)}
.abs{position:absolute}
.btn{position:absolute;display:flex;align-items:center;justify-content:center;background:linear-gradient(90deg,#2b9be0,var(--blue-dark));color:#fff;font-family:"Raleway",sans-serif;font-weight:700;font-size:18px;border-radius:4px;text-transform:uppercase}
.heading{position:absolute;left:0;width:1200px;text-align:center;font-family:"Raleway",sans-serif;font-size:40px;color:var(--blue);font-weight:300;letter-spacing:.5px}
.heading b{font-weight:800;color:var(--blue-dark)}
.para{position:absolute;font-size:15px;line-height:27px;color:var(--text)}
.img-fill{position:absolute}

/* header */
.hero-bg{left:-200px;top:-700px;width:1500px;height:1380px;border-radius:0 0 55% 45%;background:var(--sky)}
.logo{left:76px;top:18px;display:flex;align-items:center;gap:10px;font-family:"Raleway",sans-serif;font-size:22px;font-weight:600;color:var(--blue)}
.logo i{width:44px;height:44px;background:var(--blue);display:block}
.nav{right:200px;top:38px;display:flex;gap:26px;font-family:"Raleway",sans-serif;font-size:14px;font-weight:600;color:#4a5563}
.nav .active{color:var(--blue)}
.login{left:1026px;top:26px;width:96px;height:42px;font-size:16px}

.hero-kicker{left:167px;top:228px;font-family:"Raleway",sans-serif;font-weight:800;font-size:42px;color:var(--blue-dark)}
.hero-title{left:169px;top:280px;font-family:"Archivo Black",sans-serif;font-size:46px;line-height:52px;color:var(--navy)}
.hero-text{left:171px;top:334px;width:360px}

/* how to */
.step{position:absolute;width:280px;text-align:center}
.step h3{font-family:"Raleway",sans-serif;font-weight:700;font-size:19px;color:var(--blue-dark);margin:16px 0 10px}
.step p{font-size:15px;line-height:27px}

/* about */
.band{position:absolute;left:0;width:1200px;background:var(--sky)}
.about-kicker{left:582px;top:1308px;font-family:"Raleway",sans-serif;font-weight:700;font-size:21px;color:var(--blue-dark)}
.about-title{left:580px;top:1342px;font-family:"Raleway",sans-serif;font-size:41px;font-weight:300;color:var(--blue)}
.about-title b{font-weight:800;color:var(--blue-dark)}

/* problem */
.prob h4{position:absolute;font-family:"Raleway",sans-serif;font-weight:700;font-size:19px;color:var(--blue-dark)}
.hex{position:absolute;width:80px;height:88px}

/* pricing */
.price-row{position:absolute;left:137px;width:929px;height:52px;display:flex;align-items:center;font-size:16px;color:#556}
.price-row.shade{background:var(--sky-row)}
.price-row span{margin-left:30px}
.card{position:absolute;background:#fff;border:2px solid var(--line);border-radius:4px}
.plan{position:absolute;width:174px;text-align:center}
.plan small{display:block;font-size:17px;color:#444}
.plan strong{display:block;font-family:"Raleway",sans-serif;font-size:34px;font-weight:800;color:var(--blue)}

/* cta */
.cta{left:0;top:3600px;width:1200px;height:142px;background:linear-gradient(90deg,#2b98dc,var(--blue-dark))}
.cta-btn{position:absolute;left:783px;top:3647px;width:177px;height:51px;border:2px solid #fff;border-radius:5px;color:#fff;font-family:"Raleway",sans-serif;font-weight:700;font-size:18px;display:flex;align-items:center;justify-content:center}

/* footer */
.footer{left:0;top:3742px;width:1200px;height:326px;background:var(--navy)}
.fcol{position:absolute;top:3780px;color:#c7d2df;font-size:14px;line-height:30px}
.fcol h5{font-family:"Raleway",sans-serif;font-weight:700;font-size:16px;color:var(--blue);margin-bottom:16px}
.social{position:absolute;top:3924px;width:40px;height:40px;border-radius:50%}
</style>
</head>
<body>

<!-- HERO -->
<div class="abs hero-bg"></div>
<div class="abs logo"><i></i>SignalForge</div>
<div class="abs nav"><span class="active">• HOME</span><span>ABOUT</span><span>BENEFITS</span><span>PRICING</span><span>CONTACT</span></div>
<div class="btn login">LOGIN</div>

<div class="abs hero-kicker">CRYPTO TRADING</div>
<div class="abs hero-title">SignalForge</div>
<p class="para hero-text" style="font-size:16px">Lorem Ipsum is simply dummy text of the printing and typesetting industry.</p>
<div class="btn" style="left:169px;top:407px;width:177px;height:51px">GET STARTED</div>

<div class="img-fill" role="img" aria-label="Laptop showing the trading strategies dashboard" style="left:679px;top:300px;width:521px;height:379px;border-radius:8px 0 0 8px;background:linear-gradient(90deg,#111 0 27%,#f4f6f8 27%);box-shadow:0 20px 40px rgba(0,0,0,.12)"></div>
<div class="img-fill" role="img" aria-label="Round coin emblem" style="left:620px;top:236px;width:102px;height:102px;border-radius:50%;background:radial-gradient(#33b3f0,#1565b4)"></div>

<!-- HOW TO -->
<div class="heading" style="top:770px">HOW TO <b>GET STARTED</b></div>
<p class="para" style="left:0;top:830px;width:1200px;text-align:center">Lorem Ipsum is simply dummy text of the printing and typesetting industry.<br>Lorem Ipsum has been the industry's standard</p>

<svg class="abs" style="left:253px;top:920px" width="100" height="110" viewBox="0 0 100 110"><polygon points="50,0 100,27 100,83 50,110 0,83 0,27" fill="#2a9be0"/><path d="M32 55a18 18 0 0 1 30-13M68 55a18 18 0 0 1-30 13" stroke="#fff" stroke-width="3" fill="none"/></svg>
<svg class="abs" style="left:550px;top:920px" width="100" height="110" viewBox="0 0 100 110"><polygon points="50,0 100,27 100,83 50,110 0,83 0,27" fill="#1f7fcb"/><rect x="28" y="36" width="44" height="30" stroke="#fff" stroke-width="3" fill="none"/><path d="M50 66v10M40 78h20" stroke="#fff" stroke-width="3"/></svg>
<svg class="abs" style="left:839px;top:920px" width="100" height="110" viewBox="0 0 100 110"><polygon points="50,0 100,27 100,83 50,110 0,83 0,27" fill="#2a9be0"/><rect x="36" y="30" width="28" height="46" rx="4" stroke="#fff" stroke-width="3" fill="none"/></svg>

<div class="step" style="left:163px;top:1040px"><h3>Connect Exchange</h3><p>Lorem Ipsum is simply dummy text of the printing and typesetting is industry Lorem Ipsum</p></div>
<div class="step" style="left:460px;top:1040px"><h3>Create or Select Strategy</h3><p>Lorem Ipsum is simply dummy text of the printing and typesetting is industry Lorem Ipsum</p></div>
<div class="step" style="left:752px;top:1040px"><h3>Automatically Rebalance</h3><p>Lorem Ipsum is simply dummy text of the printing and typesetting is industry Lorem Ipsum</p></div>

<!-- ABOUT -->
<div class="band" style="top:1240px;height:489px"></div>
<div class="img-fill" role="img" aria-label="Businessman behind glowing blue stock charts" style="left:154px;top:1315px;width:348px;height:348px;border-radius:50%;background:radial-gradient(circle at 40% 40%,#2f7be0,#0b2a6b 75%)"></div>
<div class="abs about-kicker">About Us</div>
<div class="abs about-title">SIGNAL <b>FORGE</b></div>
<p class="para" style="left:585px;top:1398px;width:430px">Lorem Ipsum is simply dummy text of the printing and typesetting industry Lorem Ipsum .</p>
<p class="para" style="left:585px;top:1466px;width:430px">Lorem Ipsum is simply dummy text of the printing and typesetting industry. Lorem Ipsum has been the industry's standard dummy text ever since the 1500s, when an unknown printer took a galley.</p>
<div class="btn" style="left:590px;top:1592px;width:172px;height:52px">LEARN MORE</div>

<!-- PROBLEM -->
<div class="heading" style="top:1785px">PROBLEM <b>WE SOLVE</b></div>
<div class="prob">
  <svg class="hex" style="left:76px;top:1884px" viewBox="0 0 80 88"><polygon points="40,0 80,22 80,66 40,88 0,66 0,22" fill="#eef4fa"/><circle cx="40" cy="44" r="18" stroke="#1f7fcb" stroke-width="2.5" fill="none"/></svg>
  <h4 style="left:196px;top:1888px">Lorem Ipsim Text</h4>
  <p class="para" style="left:192px;top:1918px;width:240px">Lorem Ipsum is simply dummy text of the printing type.</p>
  <svg class="hex" style="left:76px;top:2022px" viewBox="0 0 80 88"><polygon points="40,0 80,22 80,66 40,88 0,66 0,22" fill="#eef4fa"/><rect x="24" y="32" width="32" height="24" rx="3" stroke="#1f7fcb" stroke-width="2.5" fill="none"/></svg>
  <h4 style="left:196px;top:2025px">Lorem Ipsim Text</h4>
  <p class="para" style="left:192px;top:2055px;width:240px">Lorem Ipsum is simply dummy text of the printing type.</p>
  <svg class="hex" style="left:76px;top:2158px" viewBox="0 0 80 88"><polygon points="40,0 80,22 80,66 40,88 0,66 0,22" fill="#eef4fa"/><path d="M24 62V40M34 62V34M44 62V44M54 62V30" stroke="#1f7fcb" stroke-width="3"/></svg>
  <h4 style="left:190px;top:2156px">Lorem Ipsim Text</h4>
  <p class="para" style="left:192px;top:2190px;width:240px">Lorem Ipsum is simply dummy text of the printing type.</p>
</div>
<div class="btn" style="left:77px;top:2275px;width:177px;height:52px">GET STARTED</div>
<div class="abs" style="left:717px;top:2180px;width:134px;height:117px;border-radius:0 0 67px 67px;background:var(--blue)"></div>
<div class="img-fill" role="img" aria-label="Laptop showing the live trading terminal with order book and price chart" style="left:508px;top:1915px;width:616px;height:303px;border-radius:10px 10px 2px 2px;background:linear-gradient(100deg,#101216 0 45%,#f3f4f6 55%);box-shadow:0 14px 30px rgba(0,0,0,.18)"></div>

<!-- PRICING -->
<div class="band" style="top:2389px;height:698px"></div>
<div class="heading" style="top:2448px">OUR <b>PRICING</b></div>
<div class="card" style="left:546px;top:2574px;width:520px;height:408px"></div>
<div class="price-row shade" style="top:2665px"><span>➔&nbsp;&nbsp;Lorem Ipsum is simply text</span></div>
<div class="price-row" style="top:2717px"><span>➔&nbsp;&nbsp;Lorem Ipsum is.</span></div>
<div class="price-row shade" style="top:2769px"><span>➔&nbsp;&nbsp;Lorem Ipsum is text</span></div>
<div class="price-row" style="top:2821px"><span>➔&nbsp;&nbsp;Lorem Ipsum is simply text</span></div>
<div class="price-row shade" style="top:2873px"><span>➔&nbsp;&nbsp;Lorem Ipsum is simply text</span></div>
<div class="card" style="left:720px;top:2534px;width:174px;height:486px;background:rgba(255,255,255,.35);border-color:#9ccbec"></div>

<div class="plan" style="left:546px;top:2588px"><small>Starter</small><strong>$22</strong></div>
<div class="plan" style="left:720px;top:2568px"><small>Advanced</small><strong>$37</strong></div>
<div class="plan" style="left:894px;top:2588px"><small>Pro</small><strong>$75</strong></div>

<svg class="abs" style="left:546px;top:2665px" width="520" height="260" viewBox="0 0 520 260" fill="none" stroke="#3a8fd0" stroke-width="1.6">
  <path d="M78 26l6 6 12-13M252 26l6 6 12-13M426 26l6 6 12-13"/>
  <path d="M78 78l6 6 12-13M252 78l6 6 12-13M426 78l6 6 12-13"/>
  <path d="M80 122l12 12M92 122l-12 12M252 130l6 6 12-13M426 130l6 6 12-13"/>
  <path d="M80 174l12 12M92 174l-12 12M252 182l6 6 12-13M432 174l12 12M444 174l-12 12"/>
  <path d="M78 234l6 6 12-13M252 234l6 6 12-13M426 234l6 6 12-13"/>
</svg>
<div class="btn" style="left:578px;top:2934px;width:104px;height:40px;font-size:16px">SELECT</div>
<div class="btn" style="left:742px;top:2952px;width:124px;height:40px;font-size:16px">SELECT</div>
<div class="btn" style="left:928px;top:2934px;width:104px;height:40px;font-size:16px">SELECT</div>

<!-- BENEFITS -->
<div class="abs" style="left:167px;top:3175px;font-family:'Raleway',sans-serif;font-size:40px;line-height:46px;color:var(--blue);font-weight:300">ADDITIONAL<br><b style="font-weight:800;color:var(--blue-dark)">BENEFITS</b></div>
<p class="para" style="left:167px;top:3280px;width:410px">Lorem Ipsum is simply dummy text of the printing and typesetting industry. Lorem Ipsum has been the industry's standard dummy text ever since the 1500s, when an unknown printer took a galley.</p>
<p class="para" style="left:167px;top:3400px;width:410px">Lorem Ipsum is simply dummy text of the printing and typesetting industry Lorem Ipsum has been.</p>
<div class="btn" style="left:167px;top:3478px;width:172px;height:51px">LEARN MORE</div>
<div class="img-fill" role="img" aria-label="Hand touching a phone over a trading chart screen" style="left:687px;top:3170px;width:348px;height:348px;border-radius:50%;background:radial-gradient(circle at 60% 50%,#2b5ea8,#0d1c3d 75%)"></div>

<!-- CTA -->
<div class="abs cta"></div>
<div class="abs" style="left:387px;top:3635px;font-family:'Raleway',sans-serif;font-size:20px;color:#d6ecfb">Ready To Get Started?</div>
<div class="abs" style="left:387px;top:3667px;font-family:'Raleway',sans-serif;font-weight:700;font-size:38px;color:#fff">Join Us Right Now!</div>
<div class="cta-btn">GET STARTED</div>

<!-- FOOTER -->
<div class="abs footer"></div>
<div class="abs logo" style="top:3782px"><i></i>SignalForge</div>
<div class="abs" style="left:76px;top:3856px;font-size:14px;color:#c7d2df;line-height:34px">
  <div>☎&nbsp;&nbsp;555 014 2290</div>
  <div>✉&nbsp;&nbsp;info@signalforge.example</div>
</div>
<div class="social" style="left:76px;background:#2c5aa0"></div>
<div class="social" style="left:122px;background:#2a9be0"></div>
<div class="social" style="left:168px;background:#d9442f"></div>
<div class="social" style="left:214px;background:#1aa3c8"></div>

<div class="fcol" style="left:347px"><h5>SITEMAP</h5>Home<br>About<br>Benefits<br>Pricing<br>Contact</div>
<div class="fcol" style="left:613px"><h5>SUPPORT</h5>Location/Contact<br>Chat<br>Contact Us<br>FAQ</div>
<div class="fcol" style="left:878px;line-height:22px"><h5 style="margin-bottom:22px">NEWSLETTER</h5>Would you like to receive our<br>Exclusive update for signup !</div>
<div class="abs" style="left:876px;top:3898px;width:200px;height:46px;background:#fff;color:#555;font-size:14px;display:flex;align-items:center;padding-left:16px">Enter Email *</div>
<div class="abs" style="left:1076px;top:3898px;width:46px;height:46px;background:var(--blue);display:flex;align-items:center;justify-content:center">
  <svg width="22" height="22" viewBox="0 0 24 24" fill="none" stroke="#fff" stroke-width="2"><path d="M22 2L11 13M22 2l-7 20-4-9-9-4z"/></svg>
</div>
<div class="abs" style="left:76px;top:4006px;width:1048px;height:1px;background:#223556"></div>
<div class="abs" style="left:0;top:4024px;width:1200px;text-align:center;font-size:13px;color:#b4c0cf">©SignalForge -2019 All rights reserved.</div>

</body>
</html>
```